Create a memorable Stationary for Security Software Company

TalbrenQuay is the worldwide leader in securing the Internet. Making Internet communications and critical data secure, reliable and available everywhere has been and continues to be our ongoing vision. We are committed to staying focused on real customer needs and to developing new and innovative security solutions that redefine the security landscape.

Industry/Entity Type

Internet

Font styles to use
Serif
Sans Serif
Script

Colors
0792cd
33a6d7
85cae6

```html
<!DOCTYPE html>
<html lang="en">
<head>
<meta charset="utf-8">
<title>TalbrenQuay Stationery</title>
<link rel="stylesheet" href="https://fonts.googleapis.com/css2?family=Open+Sans:wght@400;600;700&display=swap">
<style>
  :root {
    --blue-deep: #0792cd;
    --blue-mid: #33a6d7;
    --blue-light: #85cae6;
    --paper: #ffffff;
    --ground: #e9ecee;
    --ink: #5d6870;
    --ink-soft: #9aa3a9;
  }
  * { box-sizing: border-box; margin: 0; padding: 0; }
  html, body { width: 1200px; height: 2368px; overflow: hidden; }
  body {
    background: var(--ground);
    font-family: "Open Sans", Arial, sans-serif;
    color: var(--ink);
    position: relative;
  }
  .piece {
    position: absolute;
    background: var(--paper);
    overflow: hidden;
    box-shadow: 0 4px 14px rgba(0,0,0,0.12);
  }
  .shape { position: absolute; inset: 0; }
  .brand {
    position: absolute;
    display: flex;
    align-items: center;
    gap: 8px;
    font-weight: 700;
    color: var(--blue-deep);
    letter-spacing: 0.01em;
  }
  .brand-dot {
    border-radius: 50%;
    background: var(--blue-deep);
    flex: none;
  }

  /* Letterhead */
  .letterhead { left: 60px; top: 60px; width: 520px; height: 736px; }
  .letterhead .corner { background: var(--blue-light); clip-path: polygon(0 0, 46% 0, 0 20%); }
  .letterhead .brand { right: 36px; top: 40px; font-size: 18px; }
  .letterhead .brand-dot { width: 14px; height: 14px; }
  .letter-body {
    position: absolute; left: 56px; right: 56px; top: 190px;
    font-size: 11px; line-height: 1.75;
  }
  .letter-body p { margin-bottom: 14px; }
  .letterhead .foot-band { background: var(--blue-mid); clip-path: polygon(0 97%, 100% 97%, 100% 100%, 0 100%); }
  .letterhead .foot-wedge { background: var(--blue-light); clip-path: polygon(62% 97%, 100% 91%, 100% 97%); }
  .letter-foot {
    position: absolute; left: 56px; bottom: 36px;
    font-size: 10px; color: var(--ink-soft);
  }

  /* Folder */
  .folder { left: 620px; top: 60px; width: 520px; height: 736px; background: var(--blue-light); }
  .folder .sheen { background: var(--blue-mid); opacity: 0.35; clip-path: polygon(0 0, 38% 0, 0 26%); }
  .folder .brand {
    left: 0; right: 0; top: 340px; justify-content: center;
    font-size: 30px; color: var(--blue-deep);
  }
  .folder .brand-dot { width: 24px; height: 24px; }

  /* Envelope */
  .envelope { left: 60px; top: 860px; width: 1080px; height: 540px; }
  .envelope .wedge { background: var(--blue-light); clip-path: polygon(100% 38%, 100% 100%, 40% 100%); }
  .envelope .band { background: var(--blue-mid); clip-path: polygon(0 95%, 100% 95%, 100% 100%, 0 100%); }
  .envelope .brand { left: 56px; top: 48px; font-size: 24px; }
  .envelope .brand-dot { width: 18px; height: 18px; }
  .envelope .address {
    position: absolute; left: 56px; top: 96px;
    font-size: 13px; color: var(--ink-soft);
  }

  /* Business cards */
  .card { left: 220px; width: 760px; height: 434px; }
  .card-front { top: 1440px; background: var(--blue-light); }
  .card-front .sheen { background: var(--blue-mid); opacity: 0.4; clip-path: polygon(58% 0, 100% 0, 100% 100%, 82% 100%); }
  .card-front .brand {
    left: 0; right: 0; top: 190px; justify-content: center;
    font-size: 34px;
  }
  .card-front .brand-dot { width: 26px; height: 26px; }

  .card-back { top: 1914px; }
  .card-back .corner { background: var(--blue-light); clip-path: polygon(0 0, 62% 0, 0 58%); }
  .card-back .band { background: var(--blue-mid); clip-path: polygon(0 90%, 100% 90%, 100% 100%, 0 100%); }
  .card-back .wedge { background: var(--blue-light); clip-path: polygon(55% 90%, 100% 74%, 100% 90%); }
  .contact {
    position: absolute; right: 56px; top: 70px;
    font-size: 14px; line-height: 1.7; color: var(--ink);
  }
  .contact .contact-name { font-weight: 700; color: var(--blue-deep); font-size: 16px; }
  .contact dt { display: inline; font-weight: 600; color: var(--blue-deep); }
  .contact dd { display: inline; }
  .contact div.row { white-space: nowrap; }
  .person { position: absolute; left: 56px; bottom: 80px; }
  .person-name { font-size: 28px; font-weight: 700; color: var(--blue-deep); line-height: 1.1; }
  .person-role { font-size: 15px; color: var(--ink-soft); }
</style>
</head>
<body>

<section class="piece letterhead">
  <div class="shape corner"></div>
  <div class="brand"><span class="brand-dot"></span>TalbrenQuay</div>
  <div class="letter-body">
    <p>Dear Client, thank you for choosing our security services. We protect your data and networks with care every single day.</p>
    <p>Our team monitors threats around the clock and responds quickly to keep your systems safe, reliable and available wherever you work.</p>
    <p>Please contact us with any questions about your account or new solutions.</p>
    <p>Kind regards,</p>
  </div>
  <div class="letter-foot">555 014 2280 &nbsp; www.talbrenquay.com</div>
  <div class="shape foot-wedge"></div>
  <div class="shape foot-band"></div>
</section>

<section class="piece folder">
  <div class="shape sheen"></div>
  <div class="brand"><span class="brand-dot"></span>TalbrenQuay</div>
</section>

<section class="piece envelope">
  <div class="shape wedge"></div>
  <div class="shape band"></div>
  <div class="brand"><span class="brand-dot"></span>TalbrenQuay</div>
  <div class="address">12 Harbor Row, Port Alden</div>
</section>

<section class="piece card card-front">
  <div class="shape sheen"></div>
  <div class="brand"><span class="brand-dot"></span>TalbrenQuay</div>
</section>

<section class="piece card card-back">
  <div class="shape corner"></div>
  <div class="shape wedge"></div>
  <div class="shape band"></div>
  <dl class="contact">
    <div class="row contact-name">TalbrenQuay</div>
    <div class="row"><dt>Phone:</dt> <dd>+1 555 014 2280</dd></div>
    <div class="row"><dt>Mobile:</dt> <dd>+1 555 019 7731</dd></div>
    <div class="row"><dt>Fax:</dt> <dd>+1 555 014 2281</dd></div>
    <div class="row"><dt>Website:</dt> <dd>www.talbrenquay.com</dd></div>
    <div class="row"><dt>Email:</dt> <dd>contact@talbrenquay.com</dd></div>
  </dl>
  <div class="person">
    <div class="person-name">Alden Marsh</div>
    <div class="person-role">Manager</div>
  </div>
</section>

</body>
</html>
```